Corvana Wound Care Business card design

We need a business card designed around our logo which was provided. The logo of preference is the colored. Also the colors and fonts were provided.

Target Market(s)

Our Referral partners are home health agencies.

Industry/Entity Type

Healthcare

Contact Information for Business Card

Name , Phone #, Email , Title

Requirements
Nice to have
• Creativity
Should not have
• basic

```html
<!DOCTYPE html>
<html lang="en">
<head>
<meta charset="utf-8">
<title>Corvana Wound Care – Business Card</title>
<link rel="stylesheet" href="https://fonts.googleapis.com/css2?family=Lora:wght@500;600&family=Poppins:wght@400&display=swap">
<style>
  :root {
    --stage: #929292;
    --navy: #0d3d8f;
    --ink-blue: #2b3f99;
    --brand-blue: #0a4da3;
    --panel-deep: #0c2f8a;
    --panel-bright: #0b5cc0;
    --paper-top: #e6f5f8;
    --paper-bottom: #f1fafc;
    --text-dark: #1c1c24;
    --rule: #5a5a66;
    --white: #ffffff;
  }
  * { box-sizing: border-box; margin: 0; padding: 0; }
  html, body { width: 917px; height: 1200px; overflow: hidden; }
  body {
    background: var(--stage);
    position: relative;
    font-family: "Poppins", Arial, sans-serif;
  }
  .card {
    position: absolute;
    left: 98px;
    width: 721px;
    height: 412px;
    overflow: hidden;
    background: linear-gradient(135deg, var(--panel-deep), var(--panel-bright));
    box-shadow: 0 6px 18px rgba(0,0,0,0.35);
  }
  .card--front { top: 120px; }
  .card--back { top: 668px; }
  .card__paper { position: absolute; inset: 0; }

  .brand {
    position: absolute;
    display: flex;
    align-items: center;
    color: var(--navy);
    font-family: "Lora", Georgia, serif;
    font-weight: 600;
  }
  .brand__dot {
    border-radius: 50%;
    background: var(--brand-blue);
    flex: none;
  }
  .brand__name { line-height: 1; }
  .brand__tag {
    display: block;
    text-transform: uppercase;
  }
  .card--front .brand { left: 66px; top: 130px; gap: 22px; }
  .card--front .brand__dot { width: 64px; height: 64px; }
  .card--front .brand__name { font-size: 82px; letter-spacing: -1px; }
  .card--front .brand__tag { font-size: 15px; letter-spacing: 17px; margin-top: 10px; padding-left: 6px; }

  .card--back .brand { left: 480px; top: 172px; gap: 10px; color: var(--white); }
  .card--back .brand__dot { width: 22px; height: 22px; background: var(--white); }
  .card--back .brand__name { font-size: 38px; }
  .card--back .brand__tag { font-size: 8px; letter-spacing: 7px; margin-top: 4px; }

  .site {
    position: absolute;
    font-family: "Lora", Georgia, serif;
    font-weight: 500;
    font-size: 24px;
    letter-spacing: 6px;
    color: var(--text-dark);
  }
  .site__domain { color: var(--brand-blue); }
  .card--front .site { left: 66px; top: 300px; }
  .card--back .site { left: 40px; top: 344px; }

  .tagline {
    position: absolute;
    left: 40px; top: 32px;
    font-family: "Lora", Georgia, serif;
    font-weight: 500;
    font-size: 27px;
    line-height: 30px;
    color: var(--ink-blue);
    text-transform: uppercase;
  }
  .person { position: absolute; left: 40px; top: 140px; }
  .person__name {
    font-family: "Lora", Georgia, serif;
    font-weight: 500;
    font-size: 33px;
    color: var(--ink-blue);
  }
  .person__title { font-size: 13px; color: var(--text-dark); margin-top: 2px; }
  .divider {
    position: absolute; left: 38px; top: 215px;
    width: 375px; height: 1px; background: var(--rule);
  }
  .contacts, .area {
    position: absolute;
    list-style: none;
    font-size: 17px;
    color: var(--text-dark);
  }
  .contacts { left: 38px; top: 228px; }
  .contacts li { display: flex; align-items: center; gap: 7px; height: 25px; }
  .area { left: 240px; top: 228px; display: flex; gap: 8px; line-height: 22px; }
  .icon {
    width: 19px; height: 19px; border-radius: 50%;
    background: var(--ink-blue);
    display: flex; align-items: center; justify-content: center; flex: none;
  }
  .area .icon { margin-top: 2px; }
  .icon svg { width: 12px; height: 12px; }
</style>
</head>
<body>

<section class="card card--front" aria-label="Business card front">
  <svg class="card__paper" viewBox="0 0 721 412" aria-hidden="true">
    <defs>
      <linearGradient id="paperFront" x1="0" y1="0" x2="0" y2="1">
        <stop offset="0" stop-color="#e6f5f8"/>
        <stop offset="1" stop-color="#f1fafc"/>
      </linearGradient>
    </defs>
    <path d="M0 0 H482 Q510 0 510 28 V114 H598 Q627 114 627 143 V269 Q627 298 598 298 H510 V384 Q510 412 482 412 H0 Z" fill="url(#paperFront)"/>
  </svg>
  <div class="brand">
    <span class="brand__dot"></span>
    <div>
      <span class="brand__name">Corvana</span>
      <span class="brand__tag">Wound Care</span>
    </div>
  </div>
  <p class="site">www.<span class="site__domain">corvana</span>.com</p>
</section>

<section class="card card--back" aria-label="Business card back">
  <svg class="card__paper" viewBox="0 0 721 412" aria-hidden="true">
    <defs>
      <linearGradient id="paperBack" x1="0" y1="0" x2="0" y2="1">
        <stop offset="0" stop-color="#e6f5f8"/>
        <stop offset="1" stop-color="#f1fafc"/>
      </linearGradient>
    </defs>
    <path d="M0 0 H596 Q566 0 566 30 V114 H477 Q447 114 447 144 V268 Q447 298 477 298 H566 V382 Q566 412 596 412 H0 Z" fill="url(#paperBack)"/>
  </svg>

  <h2 class="tagline">We help you heal faster so<br>you can get back to your life</h2>

  <div class="person">
    <p class="person__name">Dr. Mara Ellison</p>
    <p class="person__title">GENERAL SURGEON</p>
  </div>
  <div class="divider"></div>

  <ul class="contacts">
    <li>
      <span class="icon"><svg viewBox="0 0 24 24"><path fill="#fff" d="M6.6 10.8a15.1 15.1 0 0 0 6.6 6.6l2.2-2.2c.3-.3.7-.4 1-.2 1.1.4 2.3.6 3.6.6.6 0 1 .4 1 1V20c0 .6-.4 1-1 1A17 17 0 0 1 3 4c0-.6.4-1 1-1h3.5c.6 0 1 .4 1 1 0 1.3.2 2.5.6 3.6.1.3 0 .7-.2 1z"/></svg></span>
      678-555-0142
    </li>
    <li>
      <span class="icon"><svg viewBox="0 0 24 24"><path fill="#fff" d="M7 3h10v5H7zM4 9h16a2 2 0 0 1 2 2v6h-4v4H6v-4H2v-6a2 2 0 0 1 2-2zm4 7v3h8v-3z"/></svg></span>
      678-555-0187
    </li>
    <li>
      <span class="icon"><svg viewBox="0 0 24 24"><path fill="#fff" d="M3 5h18v14H3zm2 2v.5l7 5 7-5V7zm0 3v7h14v-7l-7 5z"/></svg></span>
      info@corvanacare.com
    </li>
  </ul>

  <div class="area">
    <span class="icon"><svg viewBox="0 0 24 24"><path fill="#fff" d="M12 2a7 7 0 0 0-7 7c0 5 7 13 7 13s7-8 7-13a7 7 0 0 0-7-7zm0 9.5A2.5 2.5 0 1 1 12 6.5a2.5 2.5 0 0 1 0 5z"/></svg></span>
    <p>Alder, Brookfield,<br>Linden &amp; Oakmere<br>Counties, GA</p>
  </div>

  <p class="site">www.<span class="site__domain">corvana</span>.com</p>

  <div class="brand">
    <span class="brand__dot"></span>
    <div>
      <span class="brand__name">Corvana</span>
      <span class="brand__tag">Wound Care</span>
    </div>
  </div>
</section>

</body>
</html>
```